Application Dashboard Skin - Non coded theme only

We are looking for a website color theme/look feel for a new .net dashboard application we are building. Target audience who will be using this are E and C level professionals. We are looking for the following:

Images of optional color themes for our existing dashboard. You can access a temporary version with no styling here: http://vantorquel.net:99/ . Application built in telerik and highcharts.

We are not looking for finished code or application skins. Our development team will take your final design (with specific colors/images/etc. provided) and apply it to the final beta version of the application.

Design considerations:
We are open to creative ideas, but please know that preference will be given to professional designs with emphasis on a consistent brand look/feel. Designs and colors should be focused on quickly identifying and processing the data.

Multiple submissions welcome.

-Pellowrin team

Target Market(s)

IT / Insurance

Industry/Entity Type

Building

Number of Pages Required

3 page

Requirements
Must have
• Application Dashboard link for design: http://vantorquel.net:99/

```html
<!DOCTYPE html>
<html lang="en">
<head>
<meta charset="utf-8">
<title>Claimview – Accuracy Results</title>
<link href="https://fonts.googleapis.com/css2?family=Roboto:wght@400;500;700&family=Roboto+Condensed:wght@400;500&display=swap" rel="stylesheet">
<style>
:root{
  --bg:#eef0f3;
  --panel:#ffffff;
  --subpanel:#f5f6f8;
  --bar:#1f2023;
  --bar-soft:#2c2f36;
  --orange:#f7931e;
  --orange-soft:#f8a542;
  --blue:#3a8ef0;
  --indigo:#5b62d6;
  --ink:#222428;
  --muted:#55585e;
  --line:#dcdfe3;
  --footer:#1c1d20;
}
*{box-sizing:border-box;margin:0;padding:0}
html,body{width:861px;height:1200px;overflow:hidden}
body{position:relative;background:var(--bg);font-family:"Roboto",sans-serif;color:var(--ink)}
.abs{position:absolute}
.header{left:0;top:0;width:861px;height:66px;background:#fff;box-shadow:0 1px 3px rgba(0,0,0,.08)}
.brand{left:38px;top:14px;display:flex;align-items:center;gap:6px;font-size:24px;font-weight:500;color:#2b2d31}
.brand-dot{width:14px;height:14px;border-radius:50%;background:var(--orange)}
.nav-item{top:10px;transform:translateX(-50%);text-align:center;font-size:12px;font-weight:500;color:#2b2d31;white-space:nowrap}
.nav-icon{display:block;margin:0 auto 4px;width:22px;height:22px}
.nav-sep{top:18px;width:1px;height:36px;background:var(--line)}
.logout{left:770px;top:6px;width:54px;height:50px;background:var(--orange);color:#fff;font-size:12px;font-weight:500;text-align:center;padding-top:5px}
.logout .nav-icon{margin-bottom:3px}
.titlebar{height:30px;background:var(--bar);color:#fff;font-size:16px;font-weight:500;padding:0 10px;display:flex;align-items:center;justify-content:space-between}
.select{width:93px;height:19px;background:#fff;color:#333;font-size:10px;display:flex;align-items:center;padding-left:6px;position:relative}
.select::after{content:"";position:absolute;right:0;top:0;width:20px;height:19px;background:#c9ccd1}
.select::before{content:"";position:absolute;right:6px;top:7px;border:4px solid transparent;border-top:5px solid #fff;z-index:1}
.panel{background:var(--panel)}
.subhead{background:var(--subpanel)}
.h2{font-size:16px;font-weight:500;color:#2b2d31}
.sub{font-size:10px;color:var(--muted)}
.tabs{left:38px;top:495px;width:497px;height:31px;background:var(--orange);display:flex;font-size:10px;font-weight:500;color:#fff}
.tab{padding:0 13px;display:flex;align-items:center}
.tab.active{background:var(--blue);width:74px;justify-content:center;padding:0}
.kpi-row{left:558px;width:260px;height:25.4px;border-bottom:1px solid var(--line);display:flex;align-items:center;font-size:9.5px;color:#333}
.kpi-row .i{width:12px;height:12px;border-radius:50%;background:#8b8e93;color:#fff;font-size:8px;font-weight:700;text-align:center;line-height:12px;margin-right:7px}
.kpi-row .v{position:absolute;left:188px;font-weight:700}
.darkbar{background:var(--bar-soft);color:#fff;font-size:15px;font-weight:500;display:flex;align-items:center;justify-content:space-between;padding:0 8px}
.footer{left:0;top:1170px;width:861px;height:30px;background:var(--footer);color:#e6e6e6;font-size:10px;display:flex;align-items:center;justify-content:center}
svg text{font-family:"Roboto",sans-serif}
svg .cond text,svg text.cond{font-family:"Roboto Condensed",sans-serif}
</style>
</head>
<body>

<header class="abs header">
  <div class="abs brand"><span>Claimview</span><span class="brand-dot"></span></div>

  <div class="abs nav-item" style="left:389px">
    <svg class="nav-icon" viewBox="0 0 22 22"><circle cx="11" cy="11" r="10" fill="none" stroke="#f7931e" stroke-width="2"/><circle cx="11" cy="11" r="5" fill="none" stroke="#333" stroke-width="1.5"/><circle cx="11" cy="11" r="1.8" fill="#333"/></svg>Accuracy Results</div>
  <div class="abs nav-sep" style="left:454px"></div>
  <div class="abs nav-item" style="left:523px">
    <svg class="nav-icon" viewBox="0 0 22 22"><circle cx="11" cy="11" r="10" fill="none" stroke="#f7931e" stroke-width="2"/><rect x="7" y="7" width="8" height="8" fill="none" stroke="#333" stroke-width="1.5"/><rect x="9.5" y="9.5" width="3" height="3" fill="#333"/></svg>Processor Accuracy</div>
  <div class="abs nav-sep" style="left:592px"></div>
  <div class="abs nav-item" style="left:643px">
    <svg class="nav-icon" viewBox="0 0 22 22"><circle cx="11" cy="11" r="10" fill="none" stroke="#f7931e" stroke-width="2"/><circle cx="11" cy="9" r="2.5" fill="#333"/><path d="M6.5 15.5c1-3 8-3 9 0z" fill="#333"/><circle cx="7" cy="10" r="1.6" fill="#333"/><circle cx="15" cy="10" r="1.6" fill="#333"/></svg>Manage Users</div>
  <div class="abs nav-sep" style="left:697px"></div>
  <div class="abs nav-item" style="left:732px">
    <svg class="nav-icon" viewBox="0 0 22 22"><circle cx="11" cy="11" r="10" fill="none" stroke="#f7931e" stroke-width="2"/><circle cx="11" cy="11" r="4.5" fill="none" stroke="#333" stroke-width="3" stroke-dasharray="2 1.5"/><circle cx="11" cy="11" r="1.5" fill="#333"/></svg>Settings</div>

  <div class="abs logout">
    <svg class="nav-icon" viewBox="0 0 22 22"><circle cx="11" cy="11" r="10" fill="none" stroke="#fff" stroke-width="2"/><path d="M9 7h-2v8h2M10 11h6M13.5 8.5 16 11l-2.5 2.5" fill="none" stroke="#fff" stroke-width="1.6"/></svg>Logout</div>
</header>

<!-- Accuracy Results: YTD overall -->
<div class="abs titlebar" style="left:38px;top:81px;width:497px">Accuracy Results<span class="select">End to End</span></div>
<div class="abs panel" style="left:38px;top:111px;width:497px;height:335px"></div>
<div class="abs subhead" style="left:38px;top:118px;width:497px;height:54px"></div>
<div class="abs h2" style="left:46px;top:128px">YTD Overall Accuracy</div>
<div class="abs sub" style="left:46px;top:149px">Click the bars to view YTD Details for the specific region</div>

<svg class="abs" style="left:38px;top:111px" width="497.6" height="334.4" viewBox="47 139 622 418">
  <defs>
    <linearGradient id="gBlue" x1="0" y1="0" x2="0" y2="1"><stop offset="0" stop-color="#3b90f1"/><stop offset="1" stop-color="#5b5fd4"/></linearGradient>
  </defs>
  <g fill="#f7931e"><rect x="622" y="167" width="7" height="4"/><rect x="622" y="179" width="7" height="4"/><rect x="622" y="191" width="7" height="4"/></g>
  <g fill="#222"><rect x="632" y="167" width="28" height="4"/><rect x="632" y="179" width="28" height="4"/><rect x="632" y="191" width="28" height="4"/></g>
  <g stroke="#e2e4e7" stroke-width="1">
    <line x1="100" y1="263" x2="650" y2="263"/><line x1="100" y1="311" x2="650" y2="311"/><line x1="100" y1="359" x2="650" y2="359"/><line x1="100" y1="407" x2="650" y2="407"/><line x1="100" y1="456" x2="650" y2="456"/><line x1="100" y1="504" x2="650" y2="504"/>
  </g>
  <g font-size="13" fill="#333" text-anchor="end">
    <text x="89" y="267">100</text><text x="89" y="315">97.5</text><text x="89" y="363">95</text><text x="89" y="411">92.5</text><text x="89" y="460">90</text><text x="89" y="508">87.5</text>
  </g>
  <g fill="#f8a542"><rect x="129" y="309" width="50" height="50"/><rect x="243" y="292" width="50" height="52"/><rect x="355" y="327" width="50" height="50"/><rect x="466" y="309" width="50" height="50"/><rect x="576" y="364" width="50" height="50"/></g>
  <g fill="url(#gBlue)"><rect x="129" y="359" width="50" height="145"/><rect x="243" y="344" width="50" height="160"/><rect x="355" y="377" width="50" height="127"/><rect x="466" y="359" width="50" height="145"/><rect x="576" y="414" width="50" height="90"/></g>
  <g font-size="12" fill="#222" text-anchor="middle">
    <text x="154" y="297">97.7%</text><text x="268" y="282">98.5%</text><text x="380" y="317">96.8%</text><text x="491" y="298">97.7%</text><text x="601" y="354">94.9%</text>
  </g>
  <g font-size="13" font-weight="500" fill="#222" text-anchor="middle">
    <text x="154" y="523">Colorado</text><text x="268" y="523">Georgia</text><text x="380" y="523">Hawaii</text><text x="491" y="523">MidAtlantic</text><text x="601" y="523">NorthWest</text>
  </g>
</svg>

<!-- Accuracy Results: error reasons -->
<div class="abs titlebar" style="left:38px;top:465px;width:497px">Accuracy Results<span class="select">End to End</span></div>
<div class="abs tabs"><span class="tab active">All Errors</span><span class="tab">Providers</span><span class="tab">Employers</span><span class="tab">Line Of Business</span></div>
<div class="abs panel" style="left:38px;top:526px;width:497px;height:304px"></div>
<div class="abs h2" style="left:50px;top:540px">Top 10 Error Reasons</div>
<div class="abs sub" style="left:50px;top:560px">All Regions</div>

<svg class="abs" style="left:38px;top:526px" width="497.6" height="303.2" viewBox="47 658 622 379">
  <g fill="#f7931e"><rect x="626" y="684" width="6" height="4"/><rect x="626" y="692" width="6" height="4"/><rect x="626" y="700" width="6" height="4"/></g>
  <g fill="#222"><rect x="635" y="684" width="19" height="4"/><rect x="635" y="692" width="19" height="4"/><rect x="635" y="700" width="19" height="4"/></g>
  <line x1="205" y1="748" x2="205" y2="972" stroke="#888"/>
  <line x1="205" y1="972" x2="652" y2="972" stroke="#888"/>
  <g fill="#4e6ee0">
    <rect x="206" y="755" width="398" height="10"/><rect x="206" y="777" width="361" height="10"/><rect x="206" y="799" width="328" height="10"/><rect x="206" y="821" width="294" height="10"/><rect x="206" y="844" width="261" height="10"/><rect x="206" y="867" width="231" height="10"/><rect x="206" y="888" width="210" height="10"/><rect x="206" y="911" width="168" height="10"/><rect x="206" y="933" width="135" height="10"/><rect x="206" y="956" width="81" height="10"/>
  </g>
  <g class="cond" font-size="11" fill="#222" text-anchor="end">
    <text x="199" y="764">Incorrect Contract..</text><text x="199" y="786">Claim Paid Incorrectly</text><text x="199" y="808">Not A Halvern Benefit Bill</text><text x="199" y="830">Incorrect Co-Pay</text><text x="199" y="852">Copay Amount Not Correct</text><text x="199" y="875">Did Not Follow Desk</text><text x="199" y="896">Did Not Follow Pnp</text><text x="199" y="918">Claim Denied in Error</text><text x="199" y="941">Unknown</text><text x="199" y="963">Denied Incorrectly</text>
  </g>
  <g font-size="11" fill="#222">
    <text x="607" y="764">72</text><text x="570" y="786">65</text><text x="537" y="808">59</text><text x="503" y="830">53</text><text x="471" y="853">46</text><text x="441" y="876">41</text><text x="419" y="897">38</text><text x="380" y="920">30</text><text x="343" y="942">25</text><text x="291" y="965">17</text>
  </g>
  <g font-size="11" fill="#333" text-anchor="middle">
    <text x="205" y="987">0</text><text x="259" y="989">10</text><text x="317" y="989">20</text><text x="375" y="989">30</text><text x="434" y="989">40</text><text x="492" y="989">50</text><text x="546" y="989">60</text><text x="600" y="989">70</text>
  </g>
  <text x="408" y="1018" font-size="12" font-weight="500" text-anchor="middle" fill="#222">Count</text>
  <text transform="translate(76 860) rotate(-90)" font-size="12" font-weight="500" text-anchor="middle" fill="#222">All Errors</text>
</svg>

<!-- Financial impact -->
<div class="abs panel" style="left:38px;top:854px;width:497px;height:294px"></div>
<div class="abs h2" style="left:50px;top:862px">Top 10 Error Reasons - Financial Impact</div>
<div class="abs sub" style="left:50px;top:883px">All Regions</div>

<svg class="abs" style="left:38px;top:854px" width="497.6" height="294.4" viewBox="47 1067 622 368">
  <g fill="#f7931e"><rect x="626" y="1087" width="6" height="4"/><rect x="626" y="1095" width="6" height="4"/><rect x="626" y="1103" width="6" height="4"/></g>
  <g fill="#222"><rect x="635" y="1087" width="19" height="4"/><rect x="635" y="1095" width="19" height="4"/><rect x="635" y="1103" width="19" height="4"/></g>
  <g stroke="#e3e5e8"><line x1="233" y1="1134" x2="233" y2="1358"/><line x1="290" y1="1134" x2="290" y2="1358"/><line x1="349" y1="1134" x2="349" y2="1358"/><line x1="462" y1="1134" x2="462" y2="1358"/><line x1="520" y1="1134" x2="520" y2="1358"/><line x1="570" y1="1134" x2="570" y2="1358"/></g>
  <line x1="180" y1="1358" x2="628" y2="1358" stroke="#888"/>
  <g fill="#5b62d6">
    <rect x="266" y="1137" width="164" height="14"/><rect x="346" y="1160" width="75" height="14"/><rect x="405" y="1182" width="2" height="14"/><rect x="386" y="1204" width="25" height="14"/><rect x="406" y="1227" width="2" height="14"/><rect x="406" y="1249" width="2" height="14"/><rect x="346" y="1271" width="84" height="14"/><rect x="406" y="1293" width="2" height="14"/><rect x="408" y="1316" width="10" height="14"/><rect x="406" y="1338" width="2" height="14"/>
  </g>
  <rect x="404" y="1182" width="3" height="14" fill="#2ab58a"/>
  <g class="cond" font-size="11" fill="#222" text-anchor="end">
    <text x="175" y="1148">Incorrect Contract..</text><text x="175" y="1170">Claim Paid Incorrectly</text><text x="175" y="1192">Not A Halvern Benefit Bill</text><text x="175" y="1214">Incorrect Co-Pay</text><text x="175" y="1236">Copay Amount Not Correct</text><text x="175" y="1259">Did Not Follow Desk</text><text x="175" y="1281">Did Not Follow Pnp</text><text x="175" y="1303">Claim Denied in Error</text><text x="175" y="1325">Unknown</text><text x="175" y="1347">Denied Incorrectly</text>
  </g>
  <g class="cond" font-size="11.5" fill="#fff">
    <text x="276" y="1148">$-65155.67</text><text x="376" y="1148">$12510.63</text><text x="376" y="1171">$2919.39</text><text x="370" y="1282">$10390.26</text>
  </g>
  <g class="cond" font-size="11.5" fill="#222" text-anchor="end">
    <text x="342" y="1171">$-26915.92</text><text x="399" y="1193">$-245</text><text x="382" y="1215">$-3898.21</text><text x="399" y="1238">$-295</text><text x="403" y="1260">$0</text><text x="339" y="1282">$-29341.33</text><text x="403" y="1304">$0</text><text x="403" y="1327">$0</text><text x="403" y="1349">$-1.81</text>
  </g>
  <g class="cond" font-size="11.5" fill="#222">
    <text x="414" y="1193">$0</text><text x="414" y="1238">$10</text><text x="423" y="1327">$331.1</text>
  </g>
  <g font-size="11" fill="#333" text-anchor="middle">
    <text x="180" y="1372">-80k</text><text x="232" y="1372">-60k</text><text x="290" y="1372">-40k</text><text x="349" y="1372">-20k</text><text x="407" y="1372">0</text><text x="462" y="1372">20k</text><text x="520" y="1372">40k</text><text x="570" y="1372">60k</text>
  </g>
  <text x="408" y="1403" font-size="12" font-weight="500" text-anchor="middle" fill="#222">Amount</text>
</svg>

<!-- KPIs -->
<div class="abs titlebar" style="left:551px;top:81px;width:276px">KPI's<span class="select" style="width:88px">AllRegions</span></div>
<div class="abs panel" style="left:551px;top:111px;width:276px;height:401px"></div>
<div class="abs subhead" style="left:551px;top:111px;width:276px;height:64px"></div>
<div class="abs" style="left:561px;top:125px;font-size:16px;font-weight:500;color:#2b2d31;line-height:20px">Overall YTD Accuracy<br>97.41%</div>

<div class="abs kpi-row" style="top:175px"><span class="i">!</span>Claims Audited:<span class="v">4859</span></div>
<div class="abs kpi-row" style="top:200.4px"><span class="i">!</span>Avg. Claims Audited per day:<span class="v">6.7</span></div>
<div class="abs kpi-row" style="top:225.8px"><span class="i">!</span>Errors Found:<span class="v">2147</span></div>
<div class="abs kpi-row" style="top:251.2px"><span class="i">!</span>Financial Impact:<span class="v">$1,462,139</span></div>
<div class="abs kpi-row" style="top:276.6px"><span class="i">!</span>Total Claims Posted:<span class="v">17,773,591</span></div>
<div class="abs kpi-row" style="top:302px"><span class="i">!</span>Total Encounter Claims:<span class="v">93,984,586</span></div>
<div class="abs kpi-row" style="top:327.4px"><span class="i">!</span>Total Auto Adjudication Claim Count:<span class="v">920,918</span></div>
<div class="abs kpi-row" style="top:352.8px"><span class="i">!</span>Total Adjustment Claim Count:<span class="v">920,918</span></div>
<div class="abs kpi-row" style="top:378.2px"><span class="i">!</span>Total Denied Claim Count:<span class="v">133,523</span></div>
<div class="abs kpi-row" style="top:403.6px"><span class="i">!</span>Total Dollars Paid:<span class="v">$5,669,835,044</span></div>
<div class="abs kpi-row" style="top:429px"><span class="i">!</span>Auto Adjudication Rate:<span class="v">$0.052</span></div>
<div class="abs kpi-row" style="top:454.4px"><span class="i">!</span>Adjustment Rate:<span class="v">1.345%</span></div>
<div class="abs kpi-row" style="top:479.8px;border-bottom:none"><span class="i">!</span>Denial Rate:<span class="v">0.751%</span></div>

<!-- Paid vs Denied -->
<div class="abs panel" style="left:551px;top:536px;width:276px;height:296px"></div>
<div class="abs" style="left:558px;top:579px;width:260px;height:253px;border:1px solid var(--line);border-top:none"></div>
<div class="abs darkbar" style="left:558px;top:544px;width:260px;height:35px">Paid Vs. Denied
  <svg width="22" height="16" viewBox="0 0 22 16"><g fill="#f7931e"><rect y="0" width="4" height="3"/><rect y="6.5" width="4" height="3"/><rect y="13" width="4" height="3"/></g><g fill="#fff"><rect x="6" y="0" width="16" height="3"/><rect x="6" y="6.5" width="16" height="3"/><rect x="6" y="13" width="16" height="3"/></g></svg></div>

<!-- Paid vs Encounter -->
<div class="abs panel" style="left:551px;top:853px;width:276px;height:295px"></div>
<div class="abs" style="left:558px;top:889px;width:260px;height:252px;border:1px solid var(--line);border-top:none"></div>
<div class="abs darkbar" style="left:558px;top:853px;width:260px;height:36px">Paid Vs. Encounter
  <svg width="22" height="16" viewBox="0 0 22 16"><g fill="#f7931e"><rect y="0" width="4" height="3"/><rect y="6.5" width="4" height="3"/><rect y="13" width="4" height="3"/></g><g fill="#fff"><rect x="6" y="0" width="16" height="3"/><rect x="6" y="6.5" width="16" height="3"/><rect x="6" y="13" width="16" height="3"/></g></svg></div>

<svg class="abs" style="left:551px;top:580px" width="276" height="560" viewBox="689 725 345 700">
  <defs>
    <linearGradient id="gPaid" x1="0" y1="0" x2="0" y2="1"><stop offset="0" stop-color="#3b94f3"/><stop offset="1" stop-color="#5b5fd4"/></linearGradient>
  </defs>
  <text x="856" y="767" font-size="16" font-weight="500" text-anchor="middle" fill="#222">0.7% Denied</text>
  <circle cx="858" cy="918" r="92" fill="url(#gPaid)"/>
  <path d="M858 918 L858 826 L862 826 Z" fill="#fff"/>
  <line x1="858" y1="880" x2="855" y2="793" stroke="#888"/>
  <path d="M850 800 L855 792 L860 800" fill="none" stroke="#888"/>
  <text x="860" y="948" font-size="21" font-weight="500" text-anchor="middle" fill="#fff">99.3%</text>
  <text x="860" y="973" font-size="16" text-anchor="middle" fill="#fff">Paid</text>

  <text x="851" y="1154" font-size="16" font-weight="500" text-anchor="middle" fill="#222">15.9% Paid</text>
  <path d="M866 1295 L866 1203 A92 92 0 1 1 817 1217 Z" fill="#5b62d6"/>
  <line x1="866" y1="1290" x2="848" y2="1168" stroke="#888"/>
  <path d="M843 1175 L848 1166 L852 1175" fill="none" stroke="#888"/>
  <text x="866" y="1327" font-size="21" font-weight="500" text-anchor="middle" fill="#fff">84.1%</text>
  <text x="866" y="1350" font-size="16" text-anchor="middle" fill="#fff">Encounter</text>
</svg>

<footer class="abs footer">Copyright © 2016 Claimview.&nbsp; |&nbsp; All rights reserved.</footer>

</body>
</html>
```